Leonard Vasto Card

My father, Leonard Vasto, just retired at 69 years old and he needs a new business/social card that looks professional and includes some sort of logo - perhaps his initials LV. It needs to include his phone number and email address and that's it. So fairly limited text but still elegant.

Industry/Entity Type

Business

```html
<!DOCTYPE html>
<html lang="en">
<head>
<meta charset="utf-8">
<title>Leonard Vasto – Business Card</title>
<link href="https://fonts.googleapis.com/css2?family=Libre+Baskerville:wght@400&family=Open+Sans:wght@400&display=swap" rel="stylesheet">
<style>
  :root {
    --stage: #141414;
    --navy: #1c3c78;
    --royal: #2a66bd;
    --deep: #12306a;
    --paper: #f7f8fa;
    --ghost: #e6e9ef;
    --band-light: #8fb0d6;
    --band-dark: #2c5595;
    --ink: #444a55;
    --white: #ffffff;
  }
  * { margin: 0; padding: 0; box-sizing: border-box; }
  html, body { width: 1200px; height: 900px; overflow: hidden; background: var(--stage); }
  .canvas {
    position: relative; width: 1200px; height: 900px;
    display: flex; align-items: center; justify-content: center; gap: 60px;
  }
  .card {
    position: relative; width: 500px; height: 290px; border-radius: 18px; overflow: hidden;
    box-shadow: 0 14px 30px rgba(0,0,0,0.55);
  }
  .card-front {
    background: radial-gradient(ellipse at 50% 50%, var(--royal) 0%, #1f4f9c 45%, var(--deep) 100%);
    display: flex; align-items: center; justify-content: center;
  }
  .monogram-front {
    font-family: "Libre Baskerville", serif; font-weight: 400;
    font-size: 120px; color: var(--white); letter-spacing: -4px;
  }
  .card-back { background: var(--paper); }
  .monogram-ghost {
    position: absolute; left: 150px; top: 20px;
    font-family: "Libre Baskerville", serif; font-weight: 400;
    font-size: 250px; line-height: 1; color: var(--ghost); letter-spacing: -10px;
  }
  .monogram-back {
    position: absolute; left: 36px; top: 22px;
    font-family: "Libre Baskerville", serif; font-weight: 400;
    font-size: 54px; line-height: 1; color: var(--navy); letter-spacing: -2px;
  }
  .rule-top {
    position: absolute; left: 0; right: 0; top: 96px; height: 1px; background: var(--navy); opacity: .7;
  }
  .contact {
    position: absolute; right: 28px; bottom: 42px; text-align: right;
  }
  .contact-name {
    font-family: "Libre Baskerville", serif; font-size: 17px; color: var(--navy);
    padding-bottom: 4px; border-bottom: 1px solid var(--navy); margin-bottom: 10px;
    padding-left: 30px;
  }
  .contact-line {
    font-family: "Open Sans", sans-serif; font-size: 13px; color: var(--ink);
    display: flex; align-items: center; justify-content: flex-end; gap: 8px; margin-top: 5px;
  }
  .contact-icon { width: 14px; height: 12px; }
  .band {
    position: absolute; left: 0; right: 0; bottom: 0; height: 16px;
    background: linear-gradient(to bottom, var(--band-light) 0 6px, var(--band-dark) 6px);
  }
</style>
</head>
<body>
  <main class="canvas">
    <section class="card card-front" aria-label="Card front">
      <span class="monogram-front">LV</span>
    </section>

    <section class="card card-back" aria-label="Card back">
      <span class="monogram-ghost" aria-hidden="true">LV</span>
      <span class="monogram-back">LV</span>
      <div class="rule-top"></div>
      <div class="contact">
        <p class="contact-name">Leonard Vasto</p>
        <p class="contact-line">0198 765 432
          <svg class="contact-icon" viewBox="0 0 14 12" aria-hidden="true">
            <rect width="14" height="12" rx="2" fill="#2c5595"/>
            <path d="M4.5 2.5c-.8 0-1.2.8-1 1.6.5 2 1.9 3.6 4 4.4.8.3 1.6 0 1.8-.7l.2-.7-1.6-.8-.6.6c-.9-.4-1.6-1.1-2-2l.6-.6-.8-1.6z" fill="#ffffff"/>
          </svg>
        </p>
        <p class="contact-line">leonardvasto@postline.net
          <svg class="contact-icon" viewBox="0 0 14 12" aria-hidden="true">
            <rect width="14" height="12" rx="2" fill="#2c5595"/>
            <rect x="3" y="3.5" width="8" height="5.5" fill="none" stroke="#ffffff" stroke-width="1"/>
            <path d="M3 3.5l4 3 4-3" fill="none" stroke="#ffffff" stroke-width="1"/>
          </svg>
        </p>
      </div>
      <div class="band"></div>
    </section>
  </main>
</body>
</html>
```